Commercial Business Card - stand out, clean, simple, unique.

commercial real estate group located in Texas. Called 4 Ridges Real Estate. We want a unique yet clean and professional card. On one side I would like the 4R to be by itself or to look as unique or tasteful as possible. We have the logo in white, black, and color in case a black background or something similar looks best on one side. We need a space for our name, email, cell. website. And possibly room for a phrase or city.

Contact Information for Business Card

Name, Title, Email, Phone Number, website

```html
<!DOCTYPE html>
<html lang="en">
<head>
<meta charset="UTF-8">
<title>4 Ridges Real Estate – Business Card</title>
<link rel="stylesheet" href="https://fonts.googleapis.com/css2?family=Cinzel:wght@700&family=Lato:wght@400&display=swap">
<style>
  :root {
    --backdrop: #2b2b2b;
    --card: #ffffff;
    --navy: #1c2f6b;
    --navy-deep: #14214d;
    --orange: #d9622b;
    --ink: #1a1a1a;
    --rule: #3a3a3a;
  }
  * { margin: 0; padding: 0; box-sizing: border-box; }
  html, body {
    width: 1200px; height: 1200px; overflow: hidden;
    background: var(--backdrop);
  }
  .canvas { position: relative; width: 1200px; height: 1200px; }

  .card {
    position: absolute; left: 240px; width: 720px; height: 410px;
    background: var(--card); border-radius: 30px; overflow: hidden;
  }
  .card::after {
    content: ""; position: absolute; left: 0; right: 0; bottom: 0; height: 9px;
  }
  .card--front { top: 144px; }
  .card--front::after { background: var(--orange); }
  .card--back { top: 598px; }
  .card--back::after { background: var(--navy); }

  /* Front */
  .brand-name {
    position: absolute; left: 0; right: 0; top: 150px;
    text-align: center;
    font-family: "Cinzel", serif; font-weight: 700;
    font-size: 44px; letter-spacing: 1px; color: var(--navy-deep);
  }
  .front-web {
    position: absolute; left: 0; right: 0; top: 356px;
    text-align: center;
    font-family: "Lato", sans-serif; font-size: 16px;
    letter-spacing: 2.4px; color: var(--navy-deep);
  }

  /* Back */
  .brand-mark {
    position: absolute; left: 61px; top: 146px; width: 240px;
    display: flex; flex-direction: column; align-items: center; gap: 14px;
  }
  .brand-mark__dot {
    width: 84px; height: 84px; border-radius: 50%; background: var(--navy);
  }
  .brand-mark__name {
    font-family: "Lato", sans-serif; font-size: 17px; color: var(--navy);
    white-space: nowrap;
  }
  .divider {
    position: absolute; left: 306px; top: 126px;
    width: 1.5px; height: 178px; background: var(--rule);
  }
  .person { position: absolute; left: 353px; top: 134px; }
  .person__name {
    font-family: "Cinzel", serif; font-weight: 700;
    font-size: 30px; letter-spacing: 1px; color: var(--navy-deep); line-height: 1;
  }
  .person__title {
    margin-top: 6px;
    font-family: "Lato", sans-serif; font-size: 18px; color: var(--ink);
  }
  .contacts { list-style: none; margin-top: 12px; }
  .contacts li {
    display: flex; align-items: center; gap: 12px; height: 28px;
    font-family: "Lato", sans-serif; font-size: 17px; color: var(--ink);
  }
  .contacts svg { width: 15px; height: 15px; flex: none; }
</style>
</head>
<body>
<main class="canvas">

  <section class="card card--front" aria-label="Business card front">
    <h1 class="brand-name">4 Ridges Real Estate</h1>
    <p class="front-web">www.4ridgesrealestate.com</p>
  </section>

  <section class="card card--back" aria-label="Business card back">
    <div class="brand-mark">
      <span class="brand-mark__dot"></span>
      <span class="brand-mark__name">4 Ridges Real Estate</span>
    </div>
    <div class="divider"></div>
    <div class="person">
      <h2 class="person__name">DANIEL REYES</h2>
      <p class="person__title">Founder &amp; CEO</p>
      <ul class="contacts">
        <li>
          <svg viewBox="0 0 16 16" aria-hidden="true"><path fill="#d9622b" d="M3.6 1.2l2.3 2.6-1.2 1.9c.9 2 2.6 3.7 4.6 4.6l1.9-1.2 2.6 2.3-1.3 2.4C7.3 13.4 2.6 8.7 1.2 2.5z"/></svg>
          <span>555 204 3190</span>
        </li>
        <li>
          <svg viewBox="0 0 16 16" aria-hidden="true"><rect x="1" y="3" width="14" height="10" rx="1" fill="#d9622b"/><path d="M1.5 3.8L8 9l6.5-5.2" fill="none" stroke="#fff" stroke-width="1.2"/></svg>
          <span>info@4ridgesrealestate.com</span>
        </li>
        <li>
          <svg viewBox="0 0 16 16" aria-hidden="true"><g fill="none" stroke="#d9622b" stroke-width="1.2"><circle cx="8" cy="8" r="6.5"/><ellipse cx="8" cy="8" rx="2.8" ry="6.5"/><path d="M1.5 8h13M2.6 4.8h10.8M2.6 11.2h10.8"/></g></svg>
          <span>www.4ridgesrealestate.com</span>
        </li>
      </ul>
    </div>
  </section>

</main>
</body>
</html>
```